New management consulting website

I need a 4-5 page website that I can manage in WordPress on Hostlane.example for a new management consulting company. The website is www.torvik-example.com and the company name is Torvik Group LLC. The attached spec has an example of a draft site, layout and actual copy and includes company and contact information. I have more high-res images I can send.

Must include instruction/assistance loading the site to my WordPress dashboard.

Target Market(s)

Any business, especially SAAS

Industry/Entity Type

Consultant

Coding

Coded - Design and coding required

Number of Pages Required

4 page

Font styles to use
Sans Serif

Colors
0456a4

Requirements
Must have
• Modern and stylish

```html
<!DOCTYPE html>
<html lang="en">
<head>
<meta charset="utf-8">
<title>Torvik Consulting</title>
<link href="https://fonts.googleapis.com/css2?family=Montserrat:wght@400;500;600;700&display=swap" rel="stylesheet">
<style>
:root{
  --navy:#1d3c6c;
  --navy-deep:#172f55;
  --band-blue:#2d5a8f;
  --accent:#2f65a6;
  --ink:#222;
  --body:#6a6a6a;
  --light:#f3f3f3;
  --white:#fff;
  --line:#e2e2e2;
}
*{margin:0;padding:0;box-sizing:border-box}
html,body{width:1200px;height:5168px;overflow:hidden}
body{font-family:'Montserrat',sans-serif;color:var(--ink);background:var(--white);position:relative}
.abs{position:absolute}
.photo{position:absolute}
p{font-size:11.5px;line-height:19.5px;color:var(--body)}
h2.section-title{font-size:30px;line-height:34px;font-weight:500;color:var(--navy)}
.btn{position:absolute;display:inline-block;height:38px;line-height:36px;padding:0 18px;border-radius:8px;font-size:12px;font-weight:600;letter-spacing:.5px;text-transform:uppercase}
.btn-solid{background:var(--navy);color:var(--white);border:1px solid var(--navy)}
.btn-ghost{background:transparent;color:#999;border:2px solid #ccc}
.btn-ghost.on-dark{color:#bbb;border-color:#8a9ab3}
.on-dark p,.on-dark h2{color:var(--white)}

/* header */
.site-header{position:absolute;left:0;top:0;width:1200px;height:74px;background:var(--white)}
.brand{position:absolute;left:64px;top:18px;font-size:34px;font-weight:500;color:var(--navy);letter-spacing:2px}
.phone-box{position:absolute;left:964px;top:18px;display:flex;align-items:center;gap:8px}
.phone-box .ring{width:38px;height:38px;border:2px solid var(--navy);border-radius:50%;display:flex;align-items:center;justify-content:center}
.phone-box small{display:block;font-size:10px;color:var(--navy)}
.phone-box strong{display:block;font-size:17px;color:var(--navy);font-weight:700;letter-spacing:.5px}

/* hero */
.hero{position:absolute;left:0;top:74px;width:1200px;height:638px;background:linear-gradient(180deg,#bcbcbc 0%,#7c7c7c 45%,#2b2b2b 100%)}
.hero-title{position:absolute;left:666px;top:188px;font-size:46px;line-height:56px;font-weight:600;letter-spacing:2px;color:var(--white)}
.hero-title span{color:var(--accent);display:block}
.hero p{position:absolute;left:666px;top:362px;width:360px;color:#eee;font-size:12px}
.hero .btn{left:670px;top:418px}
.arrow{position:absolute;top:278px;width:42px;height:42px;border:1px solid #fff;border-radius:50%;display:flex;align-items:center;justify-content:center}

/* above band */
.above{position:absolute;left:0;top:712px;width:1200px;height:422px;background:linear-gradient(180deg,#3a6596 0%,#2a5588 60%,#234b7c 100%);text-align:center}
.above h2{position:absolute;left:0;width:1200px;top:132px;font-size:30px;font-weight:500;color:var(--white)}
.above p{position:absolute;left:400px;width:400px;color:#e8eef6}
.above .btn{left:534px;top:304px;border:1px solid #fff;color:#fff;background:transparent;font-weight:500;height:40px;line-height:38px;padding:0 20px}

/* feature rows */
.feature{position:absolute}
.frame{position:absolute;border:6px solid var(--navy)}
.dark-band{position:absolute;background:linear-gradient(90deg,#1c3a66 0%,#23446f 60%,#2c4c78 100%)}

/* team */
.team-title{position:absolute;left:0;width:1200px;text-align:center;font-size:32px;font-weight:500;color:var(--navy)}

/* footer */
.site-footer{position:absolute;left:0;top:4880px;width:1200px;height:250px;background:var(--white)}
.site-footer h4{font-size:15px;font-weight:600;color:var(--navy)}
.site-footer li{list-style:none;font-size:11px;color:#555;margin-bottom:9px}
.site-footer li::before{content:"–";margin-right:10px;color:var(--navy)}
.contact-line{display:flex;gap:12px;font-size:11px;color:#555;line-height:17px;margin-bottom:14px}
.footer-bar{position:absolute;left:0;top:5130px;width:1200px;height:38px;background:var(--navy);color:#fff;font-size:11px;text-align:center;line-height:38px}
</style>
</head>
<body>

<header class="site-header">
  <div class="brand">Torvik</div>
  <div class="phone-box">
    <div class="ring">
      <svg width="18" height="18" viewBox="0 0 24 24"><path d="M6.6 10.8c1.4 2.8 3.8 5.1 6.6 6.6l2.2-2.2c.3-.3.7-.4 1-.2 1.1.4 2.3.6 3.6.6.6 0 1 .4 1 1V20c0 .6-.4 1-1 1C10.6 21 3 13.4 3 4c0-.6.4-1 1-1h3.5c.6 0 1 .4 1 1 0 1.3.2 2.5.6 3.6.1.3 0 .7-.2 1L6.6 10.8z" fill="#1d3c6c"/></svg>
    </div>
    <div><small>Call Us</small><strong>555 014 0400</strong></div>
  </div>
</header>

<section class="hero" role="img" aria-label="Black and white photo of a climber helping another up a mountain ridge">
  <div class="arrow" style="left:62px"><svg width="12" height="12" viewBox="0 0 12 12"><path d="M8 1L3 6l5 5" stroke="#fff" fill="none" stroke-width="1.4"/></svg></div>
  <div class="arrow" style="left:1096px"><svg width="12" height="12" viewBox="0 0 12 12"><path d="M4 1l5 5-5 5" stroke="#fff" fill="none" stroke-width="1.4"/></svg></div>
  <h1 class="hero-title"><span>MANAGEMENT</span>CONSULTING<br>COMPANY</h1>
  <p>The word 'Torvik' originates from old Northumbrian English language and means 'above, beyond'.</p>
  <a class="btn btn-solid">Contact Us</a>
</section>

<section class="above" role="img" aria-label="Blue toned photo of mountains reflected in a calm lake">
  <h2>Above And Beyond</h2>
  <p style="top:180px">The word 'Torvik' originates from old Northumbrian English language and means 'above, beyond'.</p>
  <p style="top:232px">At Torvik Consulting our approach is to help you rise above your day-to-day business challenges, and build unique, innovative solutions to move beyond them.</p>
  <a class="btn">Learn More</a>
</section>

<!-- Strategy & Operations -->
<section class="feature" style="left:0;top:1134px;width:1200px;height:566px">
  <h2 class="section-title abs" style="left:186px;top:100px">Strategy &amp;<br>Operations</h2>
  <div class="abs" style="left:186px;top:184px;width:372px">
    <p>Strategy sets the foundation for a successful and profitable future. At Torvik Consulting we focus on helping you translate your ideas into implementable and sustainable operational strategies.</p>
    <p style="margin-top:8px">We will work with you to create a customized approach to optimize performance, establish best practice, improve quality and enhance the customer experience.</p>
    <p style="margin-top:8px">Our priority is to help you achieve operational excellence through continuous improvement. We focus on enabling you to consistently deliver quality through lean operations.</p>
  </div>
  <a class="btn btn-solid" style="left:186px;top:410px">Contact Us</a>
  <a class="btn btn-ghost" style="left:316px;top:410px">Add Items</a>
  <div class="frame" style="left:628px;top:90px;width:368px;height:392px;border-top:none;border-right:none"></div>
  <div class="photo" style="left:636px;top:78px;width:376px;height:396px;background:linear-gradient(135deg,#d9dde2 0%,#b8c3cf 50%,#7d8ea3 100%)" role="img" aria-label="Woman writing on sticky notes on a glass wall"></div>
</section>

<!-- Data Analysis -->
<section class="dark-band on-dark" style="left:0;top:1700px;width:1200px;height:486px" role="img" aria-label="Dark blue photo of a forested mountain landscape">
  <h2 class="section-title abs" style="left:186px;top:74px">Data Analysis &amp;<br>Insights</h2>
  <div class="abs" style="left:186px;top:158px;width:372px">
    <p>At Torvik Consulting we are passionate about leveraging the power of data to understand business performance, customer needs and revenue opportunities. We will help you identify the key metrics.</p>
    <p style="margin-top:8px">We will help you identify the key metrics that will offer maximum insight to focus your corporate strategy, optimize your operations and inform your decision making.</p>
    <p style="margin-top:8px">Torvik Consulting will help you use your data to improve customer engagement, drive new customer acquisition, reduce customer attrition and increase customer satisfaction.</p>
  </div>
  <a class="btn btn-solid" style="left:188px;top:378px;border-color:#4a6a96">Contact Us</a>
  <a class="btn btn-ghost on-dark" style="left:318px;top:378px">Add Items</a>
  <div class="photo" style="left:670px;top:186px;width:470px;height:300px;background:linear-gradient(160deg,#e5e9ee 0%,#9aa5b3 45%,#303a48 100%)" role="img" aria-label="Hand on a laptop keyboard with a glowing line chart overlay"></div>
</section>

<!-- Leadership Development -->
<section class="feature" style="left:0;top:2186px;width:1200px;height:576px">
  <div class="frame" style="left:194px;top:90px;width:364px;height:406px;border-top:none;border-left:none"></div>
  <div class="photo" style="left:184px;top:82px;width:360px;height:410px;background:linear-gradient(135deg,#c9ccd0 0%,#8b94a0 55%,#3b4656 100%)" role="img" aria-label="Team meeting around a conference table with a presenter standing"></div>
  <h2 class="section-title abs" style="left:656px;top:108px">Leadership<br>Development</h2>
  <div class="abs" style="left:656px;top:190px;width:340px">
    <p>Achieving exceptional performance and delighting customers is a team effort.</p>
    <p style="margin-top:8px">Torvik Consulting will work with you to understand your leadership development needs and deliver engaging and interactive workshops to drive high performance, motivation and engagement.</p>
    <p style="margin-top:8px">Our workshops will help your current or future leaders to embrace a culture of excellence, achieve peak performance and empower them to create strategies that facilitate the greater good.</p>
  </div>
  <a class="btn btn-solid" style="left:656px;top:418px">Contact Us</a>
  <a class="btn btn-ghost" style="left:786px;top:418px">Add Items</a>
</section>

<!-- Executive Leadership -->
<div class="abs" style="left:390px;top:2762px;width:810px;height:74px;background:var(--navy)"></div>
<div class="photo" style="left:1010px;top:2762px;width:190px;height:638px;background:linear-gradient(180deg,#2c4f7e 0%,#5e7895 50%,#1e3658 100%)" role="img" aria-label="Snowy mountain range under a blue sky"></div>
<section class="feature" style="left:0;top:2836px;width:1010px;height:564px;background:var(--light)">
  <h2 class="section-title abs" style="left:150px;top:84px">Executive<br>Leadership</h2>
  <div class="abs" style="left:150px;top:166px;width:340px">
    <p>Torvik Consulting can support your business during times of transformational change by providing interim Executive Leadership on a short-term basis.</p>
    <p style="margin-top:8px">We can provide experienced leadership to support you through leadership transitions, Mergers and Acquisitions, restructuring and business turn-arounds. Expert help when you need it, for as long as you need it.</p>
  </div>
  <a class="btn btn-solid" style="left:150px;top:334px">Contact Us</a>
  <a class="btn btn-ghost" style="left:280px;top:334px">Add Items</a>
  <div class="photo" style="left:632px;top:62px;width:330px;height:316px;background:linear-gradient(135deg,#f2f2f2 0%,#c7ccd2 50%,#6f7883 100%)" role="img" aria-label="Overhead view of colleagues working at a white table with laptops"></div>
</section>

<!-- Torvik Consulting -->
<section class="on-dark" style="position:absolute;left:0;top:3400px;width:1200px;height:484px;background:linear-gradient(180deg,#2e3f57 0%,#5a5a4a 45%,#1c1c1a 100%)" role="img" aria-label="Two hikers celebrating on a hilltop at sunset">
  <h2 class="section-title abs" style="left:626px;top:84px">Torvik Consulting</h2>
  <div class="abs" style="left:626px;top:132px;width:336px">
    <p>Torvik Consulting is a management consulting company with 20 year's experience working in market-leading SaaS business. We are equipped and ready to help you accelerate your business performance. We will work with you to solve operational challenges, set up lean business processes and develop your leadership team for the bright future ahead.</p>
    <p style="margin-top:14px">We offer dedicated one-on-one consulting and advisory services that are tailored to your business. We specialize in strategy development, operations management and data management.</p>
  </div>
  <a class="btn btn-solid" style="left:628px;top:386px;border-color:#4a6a96">Contact Us</a>
</section>
<div class="photo" style="left:150px;top:3292px;width:330px;height:222px;background:linear-gradient(135deg,#d8d4cc 0%,#8d8a82 55%,#45443f 100%)" role="img" aria-label="Two colleagues reviewing work on a laptop in a bright office"></div>

<!-- Our Team -->
<h2 class="team-title" style="top:3968px">Our Team</h2>
<section class="feature" style="left:0;top:4040px;width:1200px;height:340px">
  <h3 class="abs" style="left:210px;top:44px;font-size:22px;font-weight:500;color:var(--navy)">Marcus Hale</h3>
  <div class="abs" style="left:210px;top:76px;font-size:12px;color:#888">Founder and Senior Consultant</div>
  <p class="abs" style="left:210px;top:122px;width:380px">Marcus has a proven history maximizing organizational Performance by planning and prioritizing efficient workflow strategies. As a senior executive at Meridian Data Group, a publicly listed company, Marcus led large and diverse operations teams in the US And Europe.</p>
  <div class="abs" style="left:210px;top:224px;width:32px;height:32px;background:var(--navy);border-radius:4px"></div>
  <div class="abs" style="left:260px;top:232px;font-size:13px;color:var(--navy)">profile.example/marcus-hale</div>
  <div class="abs" style="left:736px;top:0;width:252px;height:266px;border:2px solid var(--navy)"></div>
  <div class="photo" style="left:716px;top:22px;width:262px;height:262px;background:linear-gradient(180deg,#e9ecef 0%,#b9c6d6 60%,#8497b0 100%)" role="img" aria-label="Portrait of the founder in a light blue shirt"></div>
</section>
<div class="abs" style="left:64px;top:4412px;width:1072px;height:1px;background:var(--line)"></div>

<!-- Origins -->
<h2 class="team-title" style="top:4482px">The Origins of 'Torvik'</h2>
<p class="abs" style="left:400px;top:4532px;width:400px;text-align:center">The word 'Torvik' originates from old Northumbrian English language and means 'above, beyond'.</p>
<div class="photo" style="left:0;top:4614px;width:398px;height:266px;background:linear-gradient(180deg,#6d6480 0%,#c9c4d0 50%,#4f5b77 100%)" role="img" aria-label="Sun rays breaking through clouds over a valley"></div>
<div class="photo" style="left:402px;top:4614px;width:396px;height:266px;background:linear-gradient(180deg,#aeb6ba 0%,#5d7148 55%,#2e3d22 100%)" role="img" aria-label="Green highland landscape with a rock pinnacle"></div>
<div class="photo" style="left:802px;top:4614px;width:398px;height:266px;background:linear-gradient(180deg,#1f3c66 0%,#3b6592 50%,#d39a4a 70%,#1b2b44 100%)" role="img" aria-label="Driftwood on a beach at sunset"></div>

<!-- Footer -->
<footer class="site-footer">
  <div class="abs" style="left:64px;top:86px;font-size:40px;font-weight:500;color:var(--navy);letter-spacing:2px">Torvik</div>
  <div class="abs" style="left:142px;top:144px;width:32px;height:32px;border:1px solid #999;border-radius:50%"></div>
  <div class="abs" style="left:182px;top:144px;width:32px;height:32px;border:1px solid #999;border-radius:50%"></div>

  <div class="abs" style="left:336px;top:46px">
    <h4>Sitemap</h4>
    <ul style="margin-top:20px">
      <li>About Us</li><li>Services</li><li>Team</li><li>Contact Us</li>
    </ul>
  </div>

  <div class="abs" style="left:612px;top:46px;width:240px">
    <h4>Contact Us</h4>
    <div style="margin-top:22px">
      <div class="contact-line"><svg width="18" height="18" viewBox="0 0 24 24"><path d="M12 2a7 7 0 0 0-7 7c0 5 7 13 7 13s7-8 7-13a7 7 0 0 0-7-7z" fill="none" stroke="#1d3c6c" stroke-width="1.6"/><circle cx="12" cy="9" r="2.5" fill="none" stroke="#1d3c6c" stroke-width="1.6"/></svg><span>2417 Linden Park Ave #410,<br>Riverton, GA 30000</span></div>
      <div class="contact-line"><svg width="18" height="18" viewBox="0 0 24 24"><rect x="3" y="5" width="18" height="14" rx="1" fill="none" stroke="#1d3c6c" stroke-width="1.6"/><path d="M3 6l9 7 9-7" fill="none" stroke="#1d3c6c" stroke-width="1.6"/></svg><span>info@torvik-example.com</span></div>
      <div class="contact-line"><svg width="18" height="18" viewBox="0 0 24 24"><path d="M6.6 10.8c1.4 2.8 3.8 5.1 6.6 6.6l2.2-2.2c.3-.3.7-.4 1-.2 1.1.4 2.3.6 3.6.6.6 0 1 .4 1 1V20c0 .6-.4 1-1 1C10.6 21 3 13.4 3 4c0-.6.4-1 1-1h3.5c.6 0 1 .4 1 1 0 1.3.2 2.5.6 3.6.1.3 0 .7-.2 1L6.6 10.8z" fill="none" stroke="#1d3c6c" stroke-width="1.6"/></svg><span>555-014-0400</span></div>
    </div>
  </div>

  <div class="abs" style="left:886px;top:46px;width:250px">
    <h4>Stay Up to Date !</h4>
    <p style="margin-top:18px;font-size:11px;line-height:17px;color:#555">Would you like to receive our exclusive update for signup !</p>
    <div style="position:relative;margin-top:14px;width:250px;height:34px;border:1px solid #ddd;font-size:11px;color:#666;line-height:32px;padding-left:14px">Enter Email *
      <div style="position:absolute;right:2px;top:2px;width:28px;height:28px;background:var(--navy);border-radius:3px;display:flex;align-items:center;justify-content:center">
        <svg width="14" height="14" viewBox="0 0 24 24"><path d="M2 11l20-8-6 19-4-8-10-3z" fill="#fff"/></svg>
      </div>
    </div>
  </div>
</footer>
<div class="footer-bar">©Torvik Consulting - 2021 All rights reserved.</div>

</body>
</html>
```